Dune Air & Plus business card

I need an awesome, double-sided business card designed with our new logo. I would like the one side black with the colored logo, and the back side is all yours. I'd like to see horizontal and vertical layouts. Get creative! Thank you.

Target Market(s)

HVAC, Heating and Cooling in Phoenix, AZ

Industry/Entity Type

HVAC

Contact Information for Business Card

We need our new logo on the card. Tom Harker, (623) 555-0142, tom@trydunesair.com, www.trydunesair.com, ROC 514273

```html
<!DOCTYPE html>
<html lang="en">
<head>
<meta charset="utf-8">
<title>Dune Air &amp; Plus – Business Card</title>
<link href="https://fonts.googleapis.com/css2?family=Roboto:wght@400;700;900&display=swap" rel="stylesheet">
<style>
  :root {
    --backdrop: #2c2c2e;
    --card-black: #232325;
    --card-black-edge: #28282b;
    --front-mark: #3b3b3f;
    --brand-blue: #0b5cc0;
    --brand-blue-light: #1384e0;
    --brand-orange: #f08a24;
    --brand-red: #e0401f;
    --text-light: #eeeeee;
    --text-white: #ffffff;
  }
  * { margin: 0; padding: 0; box-sizing: border-box; }
  html, body {
    width: 1200px;
    height: 1138px;
    overflow: hidden;
    background: var(--backdrop);
    font-family: "Roboto", Arial, sans-serif;
  }
  .card {
    position: absolute;
    width: 620px;
    height: 375px;
    border-radius: 16px;
    overflow: hidden;
    background: linear-gradient(160deg, var(--card-black-edge), var(--card-black));
  }
  .card-front { left: 272px; top: 184px; }
  .card-back  { left: 274px; top: 606px; }

  .front-wordmark {
    position: absolute;
    inset: 0;
    display: flex;
    align-items: center;
    justify-content: center;
    gap: 16px;
    color: var(--front-mark);
    font-weight: 900;
    font-size: 46px;
    letter-spacing: 1px;
  }
  .front-wordmark .dot {
    width: 30px; height: 30px; border-radius: 50%;
    background: var(--front-mark);
  }

  .back-waves { position: absolute; inset: 0; width: 620px; height: 375px; }

  .holder-name {
    position: absolute;
    left: 28px; top: 38px;
    color: var(--text-white);
    font-weight: 900;
    font-size: 24px;
    letter-spacing: 0.3px;
  }
  .licence {
    position: absolute;
    left: 28px; top: 224px;
    color: var(--text-light);
    font-size: 16px;
  }
  .contact-list {
    position: absolute;
    left: 28px; top: 258px;
    list-style: none;
  }
  .contact-list li {
    display: flex;
    align-items: center;
    gap: 12px;
    height: 24px;
    color: var(--text-light);
    font-size: 16px;
  }
  .contact-list svg { width: 16px; height: 16px; flex: none; }

  .back-wordmark {
    position: absolute;
    left: 300px; top: 225px;
    width: 300px;
    display: flex;
    align-items: center;
    justify-content: center;
    gap: 10px;
    color: var(--brand-blue-light);
    font-weight: 900;
    font-size: 30px;
  }
  .back-wordmark .dot {
    width: 20px; height: 20px; border-radius: 50%;
    background: var(--brand-blue-light);
  }
</style>
</head>
<body>

<section class="card card-front" aria-label="Card front">
  <div class="front-wordmark"><span class="dot"></span>Dune Air &amp; Plus</div>
</section>

<section class="card card-back" aria-label="Card back">
  <svg class="back-waves" viewBox="0 0 620 375" aria-hidden="true">
    <defs>
      <linearGradient id="blueBand" x1="0" y1="0" x2="1" y2="0">
        <stop offset="0" stop-color="#0a4fa8"/>
        <stop offset="1" stop-color="#1484e0"/>
      </linearGradient>
      <linearGradient id="warmBand" x1="0" y1="0" x2="1" y2="0">
        <stop offset="0" stop-color="#e0401f"/>
        <stop offset="0.55" stop-color="#ec6a22"/>
        <stop offset="1" stop-color="#f08a24"/>
      </linearGradient>
    </defs>
    <path d="M0,0 H620 V40 C560,10 470,5 380,50 C290,100 170,132 0,106 Z" fill="url(#blueBand)"/>
    <path d="M0,120 C160,150 280,130 370,78 C460,28 560,30 620,70 V84 C560,40 470,40 390,85 C290,145 160,165 0,136 Z" fill="url(#warmBand)"/>
  </svg>

  <h1 class="holder-name">TOM HARKER</h1>

  <p class="licence">ROC 514273</p>

  <ul class="contact-list">
    <li>
      <svg viewBox="0 0 16 16" aria-hidden="true"><path d="M2 6c0-2 2-3 6-3s6 1 6 3v1h-3V5.5H5V7H2z M4 8h8l1 5H3z" fill="#e8552a"/></svg>
      (623) 555-0142
    </li>
    <li>
      <svg viewBox="0 0 16 16" aria-hidden="true"><rect x="1" y="3" width="14" height="10" fill="#e8552a"/><path d="M1 3l7 6 7-6" fill="none" stroke="#232325" stroke-width="1.4"/></svg>
      tom@trydunesair.com
    </li>
    <li>
      <svg viewBox="0 0 16 16" aria-hidden="true"><circle cx="8" cy="8" r="6.5" fill="none" stroke="#e8552a" stroke-width="1.5"/><path d="M1.5 8h13M8 1.5c-3 3-3 10 0 13M8 1.5c3 3 3 10 0 13" fill="none" stroke="#e8552a" stroke-width="1.2"/></svg>
      www.trydunesair.com
    </li>
  </ul>

  <div class="back-wordmark"><span class="dot"></span>Dune Air &amp; Plus</div>
</section>

</body>
</html>
```